HVAC company business card design

We need a business card design for a HVAC company. The design must look professional. Both sides will be used. The total data to be on the business card is
Name
Position
Email
Direct Phone/Moile Phone
Company Contacts /Address, Phone, Fax, web)
All data will be submit once the design is confirmed. For generic purposes use;
Cem Orkut
Managing Director
+902324418352 (Mobile)
4718 Sokak No: 9 KGTB Alsancak IZMIR TURKEY
Tel: +902324418352 Fax : +902324418359
www.ozkivra.com.tr

Target Market(s)

HVAC

Industry/Entity Type

Business

Contact Information for Business Card

The total data to be on the business card is
Name
Position
Email
Direct Phone/Moile Phone
Cem Orkut
Managing Director
+902324418352 (Mobile)
www.ozkivra.com.tr
The BC will use both sides of the card. The front will include the full logo and the details for the business card holder. The business card can be divided into vertical/horizontal or to a special shape. The common data like the company address/phone/fax should be indicated elsewehere. The back can contain some part or the whole logo and must contain the web address.

Font styles to use
Serif
Sans Serif

Colors
0355a3
cfdfed

Requirements
Should not have
• Please be careful with the fonts, it shouldnt be too small or too big and must not interfere with the logo fonts. If you need to use a curvy shape please do not use as the logo is already curvy or use the curves from the logo (if it looks good, otherwise forget it)
• We are not in favor of pictograms, only if they are perfect use them.

```html
<!DOCTYPE html>
<html lang="en">
<head>
<meta charset="utf-8">
<title>OZKIVRA business card</title>
<link rel="stylesheet" href="https://fonts.googleapis.com/css2?family=Montserrat:wght@400;500;700&display=swap">
<style>
  :root {
    --stage: #e6e8ec;
    --paper: #ffffff;
    --navy: #414b66;
    --ink: #2e3650;
    --blue: #3a74c9;
    --white: #ffffff;
    --muted: #dfe4ef;
  }
  * { box-sizing: border-box; margin: 0; padding: 0; }
  html, body { width: 1200px; height: 900px; overflow: hidden; }
  body {
    background: var(--stage);
    font-family: "Montserrat", sans-serif;
    position: relative;
  }
  .card {
    position: absolute;
    left: 290px;
    width: 620px;
    height: 360px;
    border-radius: 22px;
    overflow: hidden;
  }
  /* front */
  .card-front { top: 50px; background: var(--paper); }
  .brand {
    position: absolute;
    left: 150px;
    top: 120px;
    display: flex;
    align-items: center;
    gap: 16px;
  }
  .brand-dot {
    width: 46px; height: 46px;
    border-radius: 50%;
    background: var(--blue);
  }
  .brand-name {
    font-weight: 700;
    font-size: 50px;
    letter-spacing: 2px;
    color: var(--ink);
  }
  .front-rule {
    position: absolute;
    left: 0; top: 300px;
    width: 380px; height: 1.5px;
    background: var(--blue);
  }
  .front-web {
    position: absolute;
    right: 48px; top: 282px;
    font-size: 19px;
    letter-spacing: 1.5px;
    color: var(--ink);
  }
  .front-foot {
    position: absolute;
    left: 0; bottom: 14px;
    width: 320px; height: 1.5px;
    background: var(--blue);
  }
  /* back */
  .card-back { top: 490px; background: var(--navy); color: var(--white); }
  .back-tab {
    position: absolute;
    right: 0; top: 16px;
    width: 16px; height: 28px;
    background: var(--blue);
  }
  .holder {
    position: absolute;
    right: 40px; top: 20px;
    text-align: right;
  }
  .holder-name { font-weight: 700; font-size: 22px; color: var(--blue); }
  .holder-title { font-size: 14px; letter-spacing: 0.5px; margin-top: 2px; }
  .back-rule {
    position: absolute;
    left: 50px; top: 68px;
    width: 340px; height: 1.5px;
    background: var(--blue);
  }
  .address {
    position: absolute;
    right: 40px; top: 110px;
    text-align: right;
    font-size: 14px;
    line-height: 1.45;
  }
  .contacts {
    position: absolute;
    right: 22px; top: 180px;
    list-style: none;
    font-size: 14px;
    line-height: 1.45;
  }
  .contacts li { display: flex; justify-content: flex-end; align-items: center; gap: 8px; }
  .contacts svg { width: 10px; height: 10px; fill: var(--muted); }
  .back-brand {
    position: absolute;
    left: 70px; top: 220px;
    font-weight: 700;
    font-size: 38px;
    letter-spacing: 2px;
    color: var(--blue);
  }
  .back-band {
    position: absolute;
    left: 0; bottom: 0;
    width: 100%; height: 20px;
    display: flex;
  }
  .band-blue-left { width: 30%; background: var(--blue); }
  .band-white { width: 45%; background: var(--white); }
  .band-blue-right { width: 25%; background: var(--blue); }
</style>
</head>
<body>
  <section class="card card-front">
    <div class="brand">
      <span class="brand-dot"></span>
      <span class="brand-name">OZKIVRA</span>
    </div>
    <div class="front-rule"></div>
    <p class="front-web">www.ozkivra.com.tr</p>
    <div class="front-foot"></div>
  </section>

  <section class="card card-back">
    <div class="back-tab"></div>
    <div class="holder">
      <p class="holder-name">Cem Orkut</p>
      <p class="holder-title">MANAGING DIRECTOR</p>
    </div>
    <div class="back-rule"></div>
    <address class="address" style="font-style:normal">
      4718 Sokak No: 9<br>
      KGTB Alsancak IZMIR TURKEY
    </address>
    <ul class="contacts">
      <li>+902324418352 <svg viewBox="0 0 10 10"><rect x="2" y="0" width="6" height="10" rx="1"/></svg></li>
      <li>+902324418352 <svg viewBox="0 0 10 10"><path d="M1 1 L4 1 L5 3 L3.5 4.5 Q5 7 6 6.5 L7.5 5 L9 6 L9 9 Q1 9 1 1Z"/></svg></li>
      <li>+902324418359 <svg viewBox="0 0 10 10"><rect x="1" y="3" width="8" height="6"/><rect x="3" y="0" width="4" height="3"/></svg></li>
      <li>info@cemorkut.com.tr <svg viewBox="0 0 10 10"><rect x="0" y="2" width="10" height="6"/></svg></li>
      <li>www.ozkivra.com.tr <svg viewBox="0 0 10 10"><circle cx="5" cy="5" r="4.5"/></svg></li>
    </ul>
    <p class="back-brand">OZKIVRA</p>
    <div class="back-band">
      <span class="band-blue-left"></span>
      <span class="band-white"></span>
      <span class="band-blue-right"></span>
    </div>
  </section>
</body>
</html>
```